Zielgruppe
Wir sind ein Reisebüro (online und offline) mit dem Schwerpunkt Pauschalflugreisen, individuelle Flugreisen sowie Kreuzfahrten. Unsere Zielgruppe ist bunt gemischt, eher aber mit etwas gehobeneren, der heutigen Zeit entsprechenden Ansprüchen. Es sind Kunden, die mehr Wert auf qualifizierte Beratung legen und nicht auf der "geiz ist geil" Schiene fahren.
Aufgabenstellung
Wir benötigen Briefpapier, Visitenkarten, Katalogaufkleber und Stempel mit typischen Angaben, auf dem Briefpapier inkl. der Bankverbindung.

```html
<!DOCTYPE html>
<html lang="de">
<head>
<meta charset="utf-8">
<title>FernKompass.de – Visitenkarte</title>
<link href="https://fonts.googleapis.com/css2?family=Exo+2:wght@500;600;700&display=swap" rel="stylesheet">
<style>
  :root {
    --page-bg: #e9e6da;
    --card-deep: #0b2748;
    --card-mid: #123d66;
    --card-light: #1d5a8a;
    --accent-blue: #6fb8e8;
    --brand-blue: #3a8fd0;
    --text-white: #f4f7fb;
    --curve-white: rgba(255,255,255,0.85);
    --curve-soft: rgba(150,200,240,0.35);
  }
  * { margin: 0; padding: 0; box-sizing: border-box; }
  html, body { width: 1000px; height: 1200px; overflow: hidden; }
  body {
    background: var(--page-bg);
    font-family: "Exo 2", "Helvetica Neue", Arial, sans-serif;
    position: relative;
  }
  .card {
    position: absolute;
    left: 90px;
    width: 820px;
    height: 520px;
    overflow: hidden;
    background: linear-gradient(135deg, var(--card-deep) 0%, var(--card-mid) 55%, var(--card-light) 100%);
    box-shadow: 0 8px 18px rgba(0,0,0,0.3);
  }
  .card-front { top: 45px; }
  .card-back { top: 625px; }
  .card-waves { position: absolute; inset: 0; width: 100%; height: 100%; }

  .brand-small {
    position: absolute; left: 60px; top: 110px;
    display: flex; align-items: center; gap: 12px;
    font-size: 38px; font-weight: 600; color: var(--brand-blue);
    white-space: nowrap;
  }
  .brand-dot { width: 18px; height: 18px; border-radius: 50%; background: var(--brand-blue); flex: none; }

  .partner-names {
    position: absolute; left: 80px; top: 235px;
    font-size: 48px; font-weight: 700; color: var(--accent-blue);
    white-space: nowrap;
  }
  .address {
    position: absolute; left: 90px; top: 340px;
    font-size: 27px; font-weight: 600; font-style: normal;
    line-height: 1.25; color: var(--text-white);
  }
  .contact-list {
    position: absolute; left: 430px; top: 330px;
    list-style: none; color: var(--text-white);
    font-size: 20px; font-weight: 500;
  }
  .contact-list li { display: flex; align-items: center; gap: 18px; height: 40px; white-space: nowrap; }
  .contact-icon { width: 30px; height: 24px; fill: var(--text-white); flex: none; }

  .brand-large {
    position: absolute; left: 110px; top: 255px;
    display: flex; align-items: center; gap: 16px;
    font-size: 72px; font-weight: 600; color: var(--text-white);
    white-space: nowrap;
  }
  .brand-large .brand-dot { width: 28px; height: 28px; background: var(--accent-blue); }
  .web-address {
    position: absolute; left: 380px; top: 365px;
    font-size: 30px; font-weight: 600; color: var(--brand-blue);
    white-space: nowrap;
  }
</style>
</head>
<body>

<section class="card card-front" aria-label="Visitenkarte Vorderseite">
  <svg class="card-waves" viewBox="0 0 820 520" preserveAspectRatio="none" aria-hidden="true">
    <path d="M0 80 C 250 -20, 520 0, 820 150" fill="none" stroke="var(--curve-white)" stroke-width="2"/>
    <path d="M0 150 C 200 60, 420 80, 650 280 S 820 420, 820 420" fill="none" stroke="var(--curve-soft)" stroke-width="2"/>
    <path d="M300 0 C 500 -10, 700 10, 820 40 L 820 0 Z" fill="rgba(120,190,240,0.25)"/>
  </svg>

  <div class="brand-small"><span class="brand-dot"></span>FernKompass.de</div>

  <h1 class="partner-names">Brandauer &amp; Kessel</h1>

  <address class="address">
    Lindenhofweg 8<br>
    D-65189 Talheim
  </address>

  <ul class="contact-list">
    <li>
      <svg class="contact-icon" viewBox="0 0 30 24" aria-label="Telefon" role="img">
        <path d="M2 8 C 8 2, 22 2, 28 8 L 24 11 L 21 8 L 9 8 L 6 11 Z"/>
        <rect x="7" y="11" width="16" height="11" rx="2"/>
      </svg>
      +49(0)611 – 482730
    </li>
    <li>
      <svg class="contact-icon" viewBox="0 0 30 24" aria-label="Fax" role="img">
        <rect x="9" y="1" width="10" height="7"/>
        <rect x="3" y="9" width="24" height="9" rx="1"/>
        <rect x="6" y="19" width="18" height="4"/>
      </svg>
      +49(0)611 – 4827399
    </li>
    <li>
      <svg class="contact-icon" viewBox="0 0 30 24" aria-label="E-Mail" role="img">
        <path d="M2 3 H 28 V 21 H 2 Z M2 3 L 15 14 L 28 3" fill="var(--text-white)" stroke="var(--card-mid)" stroke-width="1.5"/>
      </svg>
      service@fernkompass.de
    </li>
  </ul>
</section>

<section class="card card-back" aria-label="Visitenkarte Rückseite">
  <svg class="card-waves" viewBox="0 0 820 520" preserveAspectRatio="none" aria-hidden="true">
    <path d="M180 0 C 320 -10, 420 40, 520 110 C 620 160, 720 170, 820 190 L 820 0 Z" fill="rgba(10,35,65,0.45)"/>
    <path d="M200 20 C 330 0, 420 50, 520 110 C 600 150, 720 160, 820 175" fill="none" stroke="var(--curve-white)" stroke-width="2"/>
    <path d="M230 20 C 330 10, 400 60, 480 95" fill="none" stroke="rgba(255,255,255,0.55)" stroke-width="10" stroke-linecap="round"/>
    <path d="M0 470 C 250 460, 550 420, 820 330" fill="none" stroke="var(--curve-soft)" stroke-width="4"/>
    <path d="M300 520 C 550 480, 700 430, 820 390 L 820 520 Z" fill="rgba(110,185,235,0.3)"/>
  </svg>

  <div class="brand-large"><span class="brand-dot"></span>FernKompass.de</div>
  <p class="web-address">www.fernkompass.de</p>
</section>

</body>
</html>
```